Mara Quill Show Poster

I need some eye candy. I need a cool poster design I can use for different shows with enough blank space to insert a handwritten date, location and door price.
I don't need these things included per se - just the space to put them in for future shows. I doesn't have to be a lot of space. (see example - The Tin Lantern - $12 Nov. 1st. w/Odile Frost 8pm) I do however need my name incorporated into it - "Mara Quill" which is my name as well as my band name.
I really like what I think is called "letter press" - although I'm not sure if that is the right word. I have seen it used in posters like Vantry, Caspar Hollings, Durne, OKT - I tried to attach an example of the style below and attached one of our more recent songs incase anyone needed to hear our music for reference. thank you!!
Updates

Reason: I'm extending the dealing in hopes of getting some more submissions closer to what I'm looking for.

Just updated some more examples in hopes of giving a clearer picture. A lot of of the submissions seem to be geared towards a more dance party, Tobin Vale feel, I need an more artsy Brooklyn feel like the examples attached. I have also raised it to committed and by a few days to allow for time. Thanks!

Target Market(s)

30 somethings - hipsters

Industry/Entity Type

Club

Requirements
Must have
• letter press style
Nice to have
• the poster has to be arty and cool -
Should not have
• try to resist the urge to play off my name (Quill) - I know it's what people instinctively want to do, but I want it more arty and cool, than street dance party-ish - a lot of the submissions recently would be great for a Tobin Vale vibe, which is the opposite of what I'm going for. The examples attached, will really help explain what I am looking for!

```html
<!DOCTYPE html>
<html lang="en">
<head>
<meta charset="utf-8">
<title>Mara Quill — Show Poster</title>
<link rel="stylesheet" href="https://fonts.googleapis.com/css2?family=Share+Tech&family=Arimo:wght@700&display=swap">
<style>
  :root {
    --paper: #e3dde2;
    --ring-outer: #958690;
    --ring-gap: #e8e2e6;
    --ring-inner: #6f5462;
    --ring-line: #f5f1f4;
    --title-yellow: #f8f53c;
    --ink: #000000;
    --cyan: #1aa8e6;
    --black-body: #0c0c0c;
    --magenta: #e24c98;
    --band: #ffffff;
  }
  html, body {
    margin: 0;
    padding: 0;
    width: 776px;
    height: 1200px;
    overflow: hidden;
    background: var(--paper);
  }
  .poster {
    position: relative;
    width: 776px;
    height: 1200px;
    overflow: hidden;
    background: var(--paper);
  }
  .poster__art {
    position: absolute;
    left: 0;
    top: 0;
  }
  .instrument {
    mix-blend-mode: multiply;
  }
  .poster__title {
    position: absolute;
    left: 0;
    right: 0;
    top: 82px;
    margin: 0;
    text-align: center;
    font-family: "Share Tech", "Arial Narrow", sans-serif;
    font-weight: 400;
    font-size: 138px;
    line-height: 112px;
    letter-spacing: 12px;
    color: var(--title-yellow);
    text-shadow: 7px 7px 0 var(--ink);
  }
  .poster__title span {
    display: block;
  }
  .poster__details {
    position: absolute;
    left: 0;
    right: 0;
    top: 1133px;
    height: 67px;
    margin: 0;
    background: var(--band);
    display: flex;
    align-items: center;
    justify-content: center;
    font-family: "Arimo", Arial, sans-serif;
    font-weight: 700;
    font-size: 23px;
    color: var(--ink);
    white-space: pre;
  }
</style>
</head>
<body>
  <main class="poster">
    <svg class="poster__art" width="776" height="1200" viewBox="0 0 776 1200">
      <g class="record-rings" aria-hidden="true">
        <circle cx="400" cy="480" r="402" fill="var(--ring-outer)"/>
        <circle cx="400" cy="480" r="392" fill="none" stroke="var(--ring-line)" stroke-width="3" opacity="0.7"/>
        <circle cx="410" cy="510" r="290" fill="var(--ring-gap)"/>
        <circle cx="410" cy="512" r="276" fill="none" stroke="var(--ring-outer)" stroke-width="4" opacity="0.8"/>
        <circle cx="410" cy="515" r="260" fill="none" stroke="var(--ring-outer)" stroke-width="2" opacity="0.6"/>
        <circle cx="410" cy="518" r="246" fill="none" stroke="var(--ring-outer)" stroke-width="5" opacity="0.7"/>
        <circle cx="410" cy="520" r="232" fill="var(--ring-inner)"/>
      </g>
      <g class="instrument-trio" role="img" aria-label="Three overlapping acoustic guitar illustrations in cyan, black and magenta">
        <rect class="instrument" x="132" y="735" width="290" height="385" rx="120" fill="var(--cyan)" opacity="0.9"/>
        <rect class="instrument" x="270" y="732" width="310" height="385" rx="125" fill="var(--black-body)" opacity="0.9"/>
        <rect class="instrument" x="346" y="735" width="344" height="382" rx="125" fill="var(--magenta)" opacity="0.85"/>
      </g>
    </svg>

    <h1 class="poster__title"><span>Mara</span><span>Quill</span></h1>

    <p class="poster__details">The Tin Lantern - $12  Nov. 1st. ‘14  w/Odile Frost 8pm</p>
  </main>
</body>
</html>
```